Stationery Design Project

Would like to have the design elements we created in for our website (www.brook-holdings.example), incorporated in a stationery design layout.
Updates
Colors used in the logo attachments do not need to be used. We are open to different color variations. Looking for a crisp, clean, modern update using the design elements in attachments and which can also be viewed on or website.
A note to designers:
Project Deadline Extended
Reason: Due to update in our project description and requirements, we have decided to extend the deadline of this project to provide ample opportunity to all designers participating .
Requirements
Must have
- Must have continuity with the theme and design features used in our website. Have attached .jpg images of some of the design elements.

```html
<!DOCTYPE html>
<html lang="en">
<head>
<meta charset="utf-8">
<title>Brook Holdings Letterhead</title>
<link rel="stylesheet" href="https://fonts.googleapis.com/css2?family=Open+Sans:wght@400;600&display=swap">
<style>
  :root {
    --brand-blue: #1c80c3;
    --brand-green: #5cb947;
    --text-grey: #5a5a5a;
    --divider-grey: #b5b5b5;
    --sketch-grey: #ececec;
    --paper: #ffffff;
    --backdrop: #f2f2f2;
  }
  * { margin: 0; padding: 0; box-sizing: border-box; }
  html, body {
    width: 991px;
    height: 1200px;
    overflow: hidden;
    background: var(--backdrop);
  }
  .letterhead {
    position: relative;
    width: 991px;
    height: 1200px;
    background: var(--paper);
    font-family: "Open Sans", sans-serif;
    overflow: hidden;
  }
  .brand {
    position: absolute;
    left: 66px;
    top: 64px;
    display: flex;
    align-items: center;
    gap: 12px;
  }
  .brand-dot {
    width: 18px;
    height: 18px;
    border-radius: 50%;
    background: var(--brand-green);
  }
  .brand-name {
    font-size: 50px;
    font-weight: 400;
    color: var(--brand-blue);
    letter-spacing: -0.5px;
    line-height: 1;
  }
  .contact {
    position: absolute;
    left: 736px;
    top: 58px;
    padding-left: 11px;
    border-left: 1px solid var(--divider-grey);
    list-style: none;
    font-size: 15px;
    line-height: 19px;
    color: var(--text-grey);
  }
  .contact li {
    display: flex;
    align-items: center;
    gap: 5px;
  }
  .contact svg {
    width: 10px;
    height: 10px;
    fill: var(--brand-blue);
    flex: none;
  }
  .sketch-mark {
    position: absolute;
    left: 255px;
    top: 480px;
    width: 540px;
    height: 270px;
    border-radius: 50%;
    background: radial-gradient(ellipse at center, var(--sketch-grey) 0%, rgba(236,236,236,0) 70%);
  }
  .footer-wave {
    position: absolute;
    left: 0;
    bottom: 0;
    width: 991px;
    height: 140px;
  }
  .footer-address {
    position: absolute;
    right: 58px;
    bottom: 20px;
    font-size: 14px;
    letter-spacing: 0.6px;
    color: var(--paper);
  }
</style>
</head>
<body>
<main class="letterhead">
  <header>
    <div class="brand">
      <span class="brand-name">Brook Holdings</span>
      <span class="brand-dot"></span>
    </div>
    <ul class="contact">
      <li><svg viewBox="0 0 10 10"><path d="M2 0.5 L4 2.5 L3 3.7 Q4.2 6 6.3 7 L7.5 6 L9.5 8 L8 9.5 Q3 9 0.5 2 Z"/></svg>(555) 240-3180</li>
      <li><svg viewBox="0 0 10 10"><rect x="2.5" y="0.5" width="5" height="9" rx="1"/></svg>(555) 240-3195</li>
      <li><svg viewBox="0 0 10 10"><rect x="0.5" y="2" width="9" height="6" rx="1"/></svg>info@brook-holdings.example</li>
      <li><svg viewBox="0 0 10 10"><circle cx="5" cy="5" r="4.3"/></svg>www.brook-holdings.example</li>
    </ul>
  </header>

  <div class="sketch-mark" role="img" aria-label="Faint hand-drawn brand sketch as background decoration"></div>

  <footer>
    <svg class="footer-wave" viewBox="0 0 991 140" preserveAspectRatio="none" aria-hidden="true">
      <path fill="var(--brand-green)" d="M0,0 C150,62 310,76 510,62 C710,48 860,60 991,90 L991,140 L0,140 Z"/>
      <path fill="var(--brand-blue)" stroke="var(--paper)" stroke-width="5" d="M0,40 C150,86 320,94 520,82 C720,70 860,76 995,100 L995,145 L0,145 Z"/>
    </svg>
    <p class="footer-address">418 Millrace Lane Suite 12, Alder Falls, GA 30999</p>
  </footer>
</main>
</body>
</html>
```